Property risk and finance brokerage company needs a business card design

Tarlow Financial requires a business card design. Please integrate existing logo (refer uploaded file).
hex codes used on logo #002649 #008ED6 #444F51 #ADAFAA
font used - Cinzel
Contact information
Renata Sollisford
Director
Mobile: 0491 738 205
email: r.sollisford@tarlowfinancial.example.au
website: www.tarlowfinancial.example.au
CRN : 918354
PO Box 527
Canterbury, Victoria, 3126
Horizontal orientation please
Finance

```html
<!DOCTYPE html>
<html lang="en">
<head>
<meta charset="utf-8">
<title>Tarlow Financial – Business Card</title>
<link href="https://fonts.googleapis.com/css2?family=Source+Sans+3:ital,wght@0,400;0,600;0,700;1,400&display=swap" rel="stylesheet">
<style>
  :root {
    --navy: #002649;
    --brand-blue: #0b5fa5;
    --sky: #008ED6;
    --sky-light: #eaf6fd;
    --slate: #444F51;
    --grey-text: #7a7f80;
    --band: #231f20;
    --paper: #ffffff;
    --backdrop: #ecebe7;
  }
  html, body {
    margin: 0;
    padding: 0;
    width: 1200px;
    height: 666px;
    overflow: hidden;
    background: var(--backdrop);
    font-family: "Source Sans 3", Arial, sans-serif;
  }
  .stage {
    position: relative;
    width: 1200px;
    height: 666px;
    display: flex;
    align-items: center;
    justify-content: center;
    gap: 50px;
  }
  .card {
    position: relative;
    width: 540px;
    height: 310px;
    overflow: hidden;
    box-shadow: 0 6px 18px rgba(0,0,0,0.25);
  }
  .card__band {
    position: absolute;
    left: 0; right: 0; bottom: 0;
    height: 30px;
    background: var(--band);
  }

  /* Front */
  .card--front {
    background: radial-gradient(ellipse 70% 75% at 58% 42%, var(--paper) 0%, var(--sky-light) 18%, #7cc7ef 50%, var(--sky) 100%);
  }
  .brand-lockup {
    position: absolute;
    left: 70px;
    top: 95px;
    display: flex;
    align-items: center;
    gap: 22px;
  }
  .brand-lockup__dot {
    width: 74px;
    height: 74px;
    border-radius: 50%;
    background: var(--brand-blue);
  }
  .brand-lockup__name {
    font-weight: 600;
    color: var(--brand-blue);
    text-transform: uppercase;
    line-height: 0.95;
  }
  .brand-lockup__name span { display: block; }
  .brand-lockup__name .line-1 { font-size: 64px; letter-spacing: 1px; }
  .brand-lockup__name .line-2 { font-size: 38px; letter-spacing: 2px; }

  /* Back */
  .card--back { background: var(--paper); }
  .mini-lockup {
    position: absolute;
    left: 32px;
    top: 36px;
    display: flex;
    align-items: center;
    gap: 8px;
  }
  .mini-lockup__dot {
    width: 26px;
    height: 26px;
    border-radius: 50%;
    background: var(--brand-blue);
  }
  .mini-lockup__name {
    font-weight: 600;
    color: var(--brand-blue);
    text-transform: uppercase;
    font-size: 14px;
    line-height: 1;
    letter-spacing: 0.5px;
  }
  .mini-lockup__name span { display: block; }
  .holder {
    position: absolute;
    left: 32px;
    top: 96px;
  }
  .holder__name {
    margin: 0;
    font-size: 24px;
    font-weight: 700;
    color: var(--brand-blue);
    line-height: 1;
  }
  .holder__title {
    margin: 3px 0 0;
    font-size: 13px;
    color: var(--brand-blue);
  }
  .address {
    position: absolute;
    left: 48px;
    top: 150px;
    margin: 0;
    font-size: 15px;
    line-height: 1.3;
    color: var(--grey-text);
    font-style: normal;
  }
  .contacts {
    position: absolute;
    left: 58px;
    top: 200px;
    margin: 0;
    padding: 0;
    list-style: none;
    font-size: 14.5px;
    line-height: 1.35;
    color: var(--grey-text);
    white-space: nowrap;
  }
  .contacts__label {
    font-weight: 700;
    color: var(--brand-blue);
  }
  .contacts__divider {
    display: inline-block;
    width: 2px;
    height: 14px;
    background: var(--brand-blue);
    vertical-align: -2px;
    margin: 0 4px;
  }
</style>
</head>
<body>
<main class="stage">
  <section class="card card--front" aria-label="Business card front">
    <div class="brand-lockup">
      <div class="brand-lockup__dot"></div>
      <div class="brand-lockup__name"><span class="line-1">Tarlow</span><span class="line-2">Financial</span></div>
    </div>
    <div class="card__band"></div>
  </section>

  <section class="card card--back" aria-label="Business card back">
    <div class="mini-lockup">
      <div class="mini-lockup__dot"></div>
      <div class="mini-lockup__name"><span>Tarlow</span><span>Financial</span></div>
    </div>
    <div class="holder">
      <h1 class="holder__name">Renata Sollisford</h1>
      <p class="holder__title">Director</p>
    </div>
    <address class="address">
      PO Box 527,<br>
      Canterbury, Victoria, 3126
    </address>
    <ul class="contacts">
      <li><span class="contacts__label">Mobile :</span> 0491 738 205<span class="contacts__divider"></span><span class="contacts__label">CRN :</span> 918354</li>
      <li><span class="contacts__label">E-mail :</span> r.sollisford@tarlowfinancial.example.au</li>
      <li><span class="contacts__label">Web :</span> www.tarlowfinancial.example.au</li>
    </ul>
    <div class="card__band"></div>
  </section>
</main>
</body>
</html>
```